Pell Nutrition Therapy needs a business card design

I need a business card design for my private practice. Green is my favorite color. I would like the back of the card to include an area for future appointment dates and time. I provide nutrition therapy to individuals, groups and families. I work a lot with adolescents and women who have eating disorders, but also work with athletes.

Reason: I received several new designs and would like to take some time reviewing them.

Target Market(s)

I am working primarily with women, but also men (mostly athletes). I work with a lot of runners. I work with people who are 14-60's.

Industry/Entity Type

Nutrition

Font styles to use
Serif
Sans Serif

Colors
9bcb3c
acd037

Requirements
Nice to have
• I would love to have 'Pell' incorporated into the design since it is my last name. If possible, I'd love to have an actual moon if it looks professional.

A picture of food could also be on the card if it is simple, but not sure how it would look with Pell. I am open to ideas for both Pell and a picture of a food item.

Other font style are fine as long as they are easy to read.

```html
<!DOCTYPE html>
<html lang="en">
<head>
<meta charset="utf-8">
<title>Pell Nutrition Therapy – Business Card</title>
<link rel="stylesheet" href="https://fonts.googleapis.com/css2?family=Marcellus&family=Mulish:wght@400;700&family=Tenor+Sans&display=swap">
<style>
  :root {
    --stage: #1b1b1b;
    --front-green: #80b22e;
    --back-green: #b0d23c;
    --band-green: #5f8f0f;
    --band-line: #9cc65a;
    --sky-light: #d9e9b8;
    --ink: #141a08;
    --ink-soft: #3c4a18;
    --paper-light: #f4f8ec;
  }
  * { box-sizing: border-box; margin: 0; padding: 0; }
  html, body { width: 1200px; height: 675px; overflow: hidden; background: var(--stage); }
  .stage { position: relative; width: 1200px; height: 675px; }

  .card {
    position: absolute;
    top: 180px;
    width: 540px;
    height: 316px;
    overflow: hidden;
  }
  .card--front { left: 45px; background: var(--front-green); }
  .card--back { left: 615px; background: var(--back-green); }

  .sky-art {
    position: absolute;
    left: 0; top: 0; width: 100%;
  }
  .card--front .sky-art {
    height: 170px;
    background: linear-gradient(180deg, var(--front-green) 0%, var(--sky-light) 50%, var(--front-green) 100%);
  }
  .card--back .sky-art {
    height: 105px;
    background: linear-gradient(180deg, var(--back-green) 0%, var(--sky-light) 55%, var(--back-green) 100%);
  }

  .title-band {
    position: absolute;
    left: 0; top: 200px; width: 100%; height: 62px;
    background: var(--band-green);
    border-top: 1px solid var(--band-line);
    border-bottom: 1px solid var(--band-line);
    display: flex; align-items: center; justify-content: center;
  }
  .front-name {
    font-family: "Marcellus", serif;
    font-weight: 400;
    font-size: 26px;
    color: var(--paper-light);
    letter-spacing: 0.5px;
  }

  .back-name {
    position: absolute; left: 0; top: 116px; width: 100%;
    text-align: center;
    font-family: "Mulish", sans-serif; font-weight: 700;
    font-size: 19px; color: var(--ink); letter-spacing: 0.4px;
  }
  .service {
    position: absolute; left: 0; top: 162px; width: 100%;
    text-align: center;
  }
  .service-title {
    font-family: "Mulish", sans-serif; font-weight: 700;
    font-size: 14px; color: var(--ink);
  }
  .service-line {
    font-family: "Tenor Sans", sans-serif;
    font-size: 10.5px; color: var(--ink-soft); letter-spacing: 1.5px;
    margin-top: 3px;
  }

  .appointment {
    position: absolute; left: 0; top: 236px; width: 100%;
    display: flex; justify-content: center; gap: 40px;
    font-family: "Tenor Sans", sans-serif; font-size: 10.5px; color: var(--ink);
  }
  .field { display: flex; align-items: flex-end; gap: 4px; }
  .field-line { display: inline-block; width: 110px; border-bottom: 1px solid var(--ink); height: 10px; }

  .contact-band {
    position: absolute; left: 0; bottom: 0; width: 100%; height: 42px;
    background: var(--band-green);
    display: flex; align-items: center; justify-content: space-around;
    font-family: "Tenor Sans", sans-serif; font-size: 11.5px;
    color: var(--paper-light); letter-spacing: 0.4px;
  }
  .contact-item { display: flex; align-items: center; gap: 6px; white-space: nowrap; }
  .divider { width: 1px; height: 22px; background: var(--band-line); }
  .contact-icon { width: 12px; height: 12px; }
</style>
</head>
<body>
<main class="stage">

  <section class="card card--front" aria-label="Card front">
    <div class="sky-art" role="img" aria-label="Sky illustration with clouds and a glowing moon"></div>
    <div class="title-band">
      <h1 class="front-name">PELL NUTRITION THERAPY</h1>
    </div>
  </section>

  <section class="card card--back" aria-label="Card back">
    <div class="sky-art" role="img" aria-label="Sky illustration with clouds and a small moon"></div>
    <h2 class="back-name">PELL NUTRITION THERAPY</h2>
    <div class="service">
      <p class="service-title">LOREM IPSUM DOLOR</p>
      <p class="service-line">Lorem ipsum dolor sit amet</p>
    </div>
    <div class="appointment">
      <span class="field">DATE: <span class="field-line"></span></span>
      <span class="field">TIME: <span class="field-line"></span></span>
    </div>
    <footer class="contact-band">
      <span class="contact-item">ADDRESS: XXXXXXXXXXX</span>
      <span class="divider"></span>
      <span class="contact-item">
        <svg class="contact-icon" viewBox="0 0 12 12" aria-hidden="true">
          <rect x="3" y="0.5" width="6" height="11" rx="1.2" fill="none" stroke="#f4f8ec" stroke-width="1"/>
          <rect x="4.2" y="2" width="3.6" height="4" fill="#f4f8ec"/>
        </svg>
        XXXXXXXXXXX
      </span>
      <span class="divider"></span>
      <span class="contact-item">
        <svg class="contact-icon" viewBox="0 0 12 12" aria-hidden="true">
          <rect x="0.5" y="2.5" width="11" height="7" fill="none" stroke="#f4f8ec" stroke-width="1"/>
          <path d="M0.5 2.5 L6 7 L11.5 2.5" fill="none" stroke="#f4f8ec" stroke-width="1"/>
        </svg>
        XXXXXXXXXXX
      </span>
    </footer>
  </section>

</main>
</body>
</html>
```